Garage Door Sales and Repair Website

Looking for a website theme and home page design for a garage door sales and repair company (Cedar Ridge Overhead).   We have a new logo and color scheme (attached) and need to update our website to match.  Here is the current site http://www.cedarridgeoverhead.example/
The design should lend it self to being responsive and full screen.
I like this site (http://www.brightpane-studio.example/) how it has different color blocks and I would like to have a slide show on my home page as well.  4 slides utilizing some of the following concepts Garage Opener, Garage Doors, Springs, Garage Door Repair, Specials, Free Estimate, etc...
Would like color design to match logo / business cards attached.
Call for Free Estimate with phone number should be visible on top of the page as well.

Consumers
Professional Service
1 page
Other font styles liked:
- Oswald, Open Sans, other similar google web fonts

Requirements
Must have
- 4 slides for home page design
- Free Estimate
- Phone Number

Nice to have
- Call out for online specials

```html
<!DOCTYPE html>
<html lang="en">
<head>
<meta charset="utf-8">
<title>Cedar Ridge Overhead – Garage Door Sales and Repair</title>
<link href="https://fonts.googleapis.com/css2?family=Cinzel:wght@400;700&family=Oswald:wght@400;500&family=Lato:wght@400;700&display=swap" rel="stylesheet">
<style>
:root{
  --navy:#434b6e;
  --navy-dark:#363d5c;
  --mist:#d3dde4;
  --mist-light:#e6edf2;
  --sky:#1a9bc9;
  --sky-dark:#0f6f99;
  --orange:#f47c20;
  --ink:#2b2f3a;
  --rule:#c5ced6;
  --white:#ffffff;
}
*{box-sizing:border-box;margin:0;padding:0}
html,body{width:1200px;height:2449px;overflow:hidden}
body{position:relative;background:var(--white);font-family:"Lato",sans-serif;color:var(--ink)}
.abs{position:absolute}

/* top bar */
.topbar{left:0;top:0;width:1200px;height:46px;background:linear-gradient(90deg,#eef2f5 0%,var(--mist) 55%,#b9c8d3 100%)}
.topbar-tagline{right:330px;top:9px;color:var(--white);font-family:"Lato",sans-serif;font-weight:700;font-size:20px}
.topbar-phone{left:895px;top:0;width:305px;height:52px;background:var(--navy);clip-path:polygon(22px 0,100% 0,100% 100%,0 100%);display:flex;align-items:center;gap:10px;padding-left:48px;color:var(--white);font-size:25px;font-weight:700}

/* header */
.brand{left:56px;top:40px;display:flex;align-items:center;gap:12px}
.brand-mark{width:30px;height:30px;border-radius:50%;background:var(--navy)}
.brand-name{font-family:"Cinzel",serif;font-weight:700;font-size:25px;line-height:1.05;color:var(--navy);width:170px}
.nav{left:298px;top:96px;display:flex;gap:0}
.nav a{position:absolute;white-space:nowrap;font-family:"Cinzel",serif;font-size:17px;color:var(--ink);text-decoration:none;letter-spacing:.5px}
.nav a.active{border-bottom:2px solid var(--navy);padding-bottom:4px}

/* hero */
.hero{left:0;top:130px;width:1200px;height:495px;overflow:hidden;background:linear-gradient(100deg,#2fb4de 0%,var(--sky) 45%,var(--sky-dark) 100%)}
.hero-photo{left:0;top:70px;width:700px;height:425px;background:linear-gradient(120deg,#d9dde2 0%,#b8bec6 50%,#8d96a3 100%)}
.hero-curve{left:0;top:0;width:1200px;height:110px}
.hero-cta{left:748px;top:110px;width:260px;height:65px;background:var(--orange);border-radius:5px;border:2px solid #ffb070;display:flex;align-items:center;gap:12px;padding-left:12px;color:var(--white)}
.hero-cta small{display:block;font-size:17px;font-weight:700}
.hero-cta strong{display:block;font-size:24px}
.hero-title{left:753px;top:208px;color:var(--white);font-family:"Oswald",sans-serif;font-weight:400;text-transform:uppercase;line-height:1.22}
.hero-title .sm{font-size:24px}
.hero-title .lg{font-size:32px}
.hero-title .md{font-size:25px}
.hero-list{left:750px;top:352px;list-style:none;color:var(--white);font-weight:700;font-size:16px}
.hero-list li{display:flex;align-items:center;gap:8px;height:29px}
.hero-badge{left:1034px;top:350px;width:92px;height:92px;border-radius:50%;background:#c8a24a}
.slide-arrow{top:253px;width:34px;height:34px;border-radius:50%;background:rgba(255,255,255,.8);display:flex;align-items:center;justify-content:center}
.hero-dots{}

/* services */
.section-title{font-family:"Cinzel",serif;font-weight:400;color:var(--navy);letter-spacing:1px}
.services-title{left:0;top:668px;width:1200px;text-align:center;font-size:36px}
.services-title::before,.services-title::after{content:"";display:inline-block;width:150px;height:3px;background:linear-gradient(90deg,transparent,#9aa3b1,transparent);vertical-align:middle;margin:0 28px}
.service-card{top:754px;width:253px;height:286px;background:var(--navy);overflow:hidden}
.service-photo{width:253px;height:130px}
.service-wave{position:absolute;left:0;top:95px;width:253px;height:60px}
.service-card h3{position:absolute;top:166px;width:100%;text-align:center;font-family:"Cinzel",serif;font-weight:400;font-size:17px;color:var(--white)}
.service-card p{position:absolute;top:194px;left:22px;right:22px;text-align:center;font-size:13.5px;line-height:1.4;color:#e5e9f2}
.service-more{position:absolute;left:110px;bottom:-16px;width:34px;height:34px;border-radius:50%;background:var(--white);color:var(--navy);text-align:center;font-weight:700;line-height:28px;font-size:17px}

/* welcome band */
.band{left:0;top:1109px;width:1200px;height:423px;background:var(--mist)}
.welcome-title{left:62px;top:1148px;width:645px;font-size:26px;padding-bottom:10px;border-bottom:1px solid var(--rule)}
.welcome-text{left:62px;top:1200px;width:645px;font-size:14.4px;line-height:1.72;text-align:justify}
.btn{background:var(--navy);color:var(--white);font-size:12.5px;font-weight:700;text-transform:uppercase;border-radius:3px;text-align:center;line-height:30px;border:none}
.read-more{left:62px;top:1453px;width:101px;height:30px}
.inquiry-title{left:772px;top:1148px;width:366px;font-size:26px;padding-bottom:10px;border-bottom:1px solid var(--rule)}
.field{left:772px;width:366px;height:33px;background:var(--white);border:1px solid #c9d2da;display:flex;align-items:center;font-size:13px}
.field .ico{width:38px;height:100%;border-right:1px solid #dde3e8;display:flex;align-items:center;justify-content:center}
.field span{padding-left:12px}
.field.msg{height:94px;align-items:flex-start}
.field.msg .ico{align-items:flex-start;padding-top:8px}
.field.msg span{padding-top:8px}
.submit{left:775px;top:1455px;width:83px;height:28px;line-height:28px}

/* testimonials & offer */
.col-title{font-size:27px;padding-bottom:14px;border-bottom:2px solid #d6dde3}
.testi-title{left:60px;top:1574px;width:507px}
.offer-title{left:629px;top:1574px;width:509px}
.pager{font-size:20px;color:#8a93a4;letter-spacing:6px}
.divider{left:597px;top:1570px;width:1px;height:300px;background:#dfe4e9}
.quote{left:62px;top:1662px;width:507px;height:143px;background:var(--mist);border-radius:6px;padding:14px 24px 0 24px;font-style:italic;font-size:13.5px;line-height:1.78;color:var(--ink)}
.quote-tail{left:300px;top:1804px;width:120px;height:26px}
.avatar{left:82px;top:1795px;width:90px;height:90px;border-radius:50%;background:linear-gradient(135deg,#c9a98a,#7b6755);border:4px solid var(--white);box-shadow:0 0 0 1px #d0d6dc}
.testi-name{left:232px;top:1833px;font-size:14.5px;color:var(--navy)}
.offer-sub{left:629px;top:1659px;font-family:"Cinzel",serif;font-size:16.5px;color:var(--ink)}
.offer-text{left:629px;top:1685px;width:510px;font-size:13.5px;line-height:1.5}
.offer-box{left:629px;top:1749px;width:507px;height:117px;background:var(--mist);border-radius:6px;padding:6px 17px}
.offer-box .price{font-family:"Cinzel",serif;font-size:33px;color:var(--navy)}
.offer-box .what{font-size:24px;font-weight:700;color:var(--ink);margin-top:-2px}
.offer-box .note{font-size:15px;font-weight:700;color:var(--ink)}
.dots{position:absolute;right:12px;bottom:16px;display:flex;gap:6px}
.dots i{width:8px;height:8px;border-radius:50%;background:#9ca5b5}
.dots i:first-child{background:var(--navy)}

/* badges */
.badge{top:1951px}
.badge-award{left:69px;width:86px;height:84px;border-radius:50%;background:#c8a24a}
.badge-rect{left:200px;top:1962px;width:168px;height:65px;border-radius:8px;background:#1e1e1e}
.badge-round{left:414px;top:1958px;width:84px;height:78px;border-radius:50%;background:#f5b21b}

/* footer */
.footer-wave{left:0;top:1912px;width:1200px;height:200px}
.footer{left:0;top:2100px;width:1200px;height:300px;background:var(--navy);color:var(--white)}
.f-title{position:absolute;top:58px;font-family:"Cinzel",serif;font-size:18px;padding-bottom:8px;border-bottom:1px solid #646c8c;width:137px}
.f-sep{position:absolute;top:75px;width:1px;height:170px;background:#5b6385}
.f-links{position:absolute;left:62px;top:104px;list-style:none;font-size:12.5px;line-height:23.5px}
.f-links li::before{content:"";display:inline-block;width:5px;height:5px;border-radius:50%;background:var(--white);margin-right:10px;vertical-align:middle}
.f-contact{position:absolute;left:308px;font-size:13.5px;line-height:1.45;display:flex;gap:14px}
.f-map{position:absolute;left:639px;top:110px;width:223px;height:158px;background:linear-gradient(135deg,#eae6d8,#d6dde2);border:2px solid var(--white)}
.f-logo{position:absolute;left:950px;top:130px;display:flex;align-items:center;gap:10px;opacity:.45}
.f-logo .mark{width:26px;height:26px;border-radius:50%;background:#aab2c6}
.f-logo span{font-family:"Cinzel",serif;font-weight:700;font-size:24px;line-height:1.05;color:#aab2c6;width:170px}
.bottombar{left:0;top:2400px;width:1200px;height:49px;background:var(--mist);display:flex;align-items:center;padding:0 60px;justify-content:space-between;font-size:14px}
.social{display:flex;gap:8px}
.social i{width:29px;height:29px;border-radius:50%;display:block}
</style>
</head>
<body>

<header>
  <div class="abs topbar"></div>
  <div class="abs topbar-tagline">For All Your Garage Door Needs</div>
  <div class="abs topbar-phone">
    <svg width="26" height="26" viewBox="0 0 26 26"><circle cx="13" cy="13" r="11.5" fill="none" stroke="#fff" stroke-width="2"/><path d="M9 7.5c.8-.6 1.6 0 2 .8l.8 1.6c.3.6.1 1.2-.4 1.6l-.7.5c.6 1.4 1.7 2.6 3.1 3.2l.6-.7c.4-.5 1-.6 1.6-.3l1.6.8c.8.4 1.3 1.2.8 2-1.6 2.3-4.3 1.4-6.6-.8C9.5 13.8 7.1 10 9 7.5z" fill="#fff"/></svg>
    555-014-2290
  </div>

  <div class="abs brand">
    <div class="brand-mark"></div>
    <div class="brand-name">Cedar Ridge Overhead</div>
  </div>

  <nav class="abs nav">
    <a class="active" style="left:0">Home</a>
    <a style="left:88px">Openers</a>
    <a style="left:202px">Garage Door Repair</a>
    <a style="left:434px">Broken Springs</a>
    <a style="left:619px">Garage Doors</a>
    <a style="left:788px">Blog</a>
  </nav>
</header>

<section class="abs hero">
  <div class="abs hero-photo" role="img" aria-label="Smiling technician in a tool belt standing beside a branded service van"></div>
  <svg class="abs hero-curve" viewBox="0 0 1200 110" preserveAspectRatio="none">
    <path d="M0 0H1200V10C900 60 500 40 0 80Z" fill="#fff"/>
    <path d="M0 80C500 40 900 60 1200 10V22C900 72 500 52 0 92Z" fill="#434b6e"/>
    <path d="M0 92C500 52 900 72 1200 22V30C900 80 500 60 0 100Z" fill="#fff" opacity=".7"/>
  </svg>

  <div class="abs hero-cta">
    <svg width="40" height="40" viewBox="0 0 26 26"><circle cx="13" cy="13" r="11.5" fill="none" stroke="#fff" stroke-width="1.6"/><path d="M9 7.5c.8-.6 1.6 0 2 .8l.8 1.6c.3.6.1 1.2-.4 1.6l-.7.5c.6 1.4 1.7 2.6 3.1 3.2l.6-.7c.4-.5 1-.6 1.6-.3l1.6.8c.8.4 1.3 1.2.8 2-1.6 2.3-4.3 1.4-6.6-.8C9.5 13.8 7.1 10 9 7.5z" fill="#fff"/></svg>
    <div><small>Call for Free Estimate</small><strong>555-014-2290</strong></div>
  </div>

  <h1 class="abs hero-title">
    <span class="sm">Denver's Preferred</span><br>
    <span class="lg">Garage Door Sales</span> <span class="md">and</span><br>
    <span class="lg">Repair</span> <span class="md">Company</span>
  </h1>

  <ul class="abs hero-list">
    <li><svg width="16" height="16" viewBox="0 0 16 16"><rect x="1" y="2" width="12" height="12" rx="3" fill="none" stroke="#fff" stroke-width="1.5"/><path d="M4 8l3 3 8-9" fill="none" stroke="#fff" stroke-width="2"/></svg>New Garage Doors &amp; Door</li>
    <li><svg width="16" height="16" viewBox="0 0 16 16"><rect x="1" y="2" width="12" height="12" rx="3" fill="none" stroke="#fff" stroke-width="1.5"/><path d="M4 8l3 3 8-9" fill="none" stroke="#fff" stroke-width="2"/></svg>Opemers Broken Springs</li>
    <li><svg width="16" height="16" viewBox="0 0 16 16"><rect x="1" y="2" width="12" height="12" rx="3" fill="none" stroke="#fff" stroke-width="1.5"/><path d="M4 8l3 3 8-9" fill="none" stroke="#fff" stroke-width="2"/></svg>Garage Door Repairs</li>
  </ul>
  <div class="abs hero-badge" role="img" aria-label="Award badge"></div>

  <div class="abs slide-arrow" style="left:10px"><svg width="12" height="14" viewBox="0 0 12 14"><path d="M8 2 3 7l5 5" fill="none" stroke="#333" stroke-width="2"/></svg></div>
  <div class="abs slide-arrow" style="left:1155px"><svg width="12" height="14" viewBox="0 0 12 14"><path d="M4 2l5 5-5 5" fill="none" stroke="#333" stroke-width="2"/></svg></div>
</section>

<section>
  <h2 class="abs section-title services-title">Our Services</h2>

  <article class="abs service-card" style="left:62px">
    <div class="service-photo" role="img" aria-label="Technician repairing an overhead garage door track" style="background:linear-gradient(135deg,#d8dde3,#9aa4b0)"></div>
    <svg class="service-wave" viewBox="0 0 253 60" preserveAspectRatio="none"><path d="M0 30C80 0 170 0 253 22V60H0Z" fill="#fff"/><path d="M0 42C80 14 170 14 253 34V60H0Z" fill="#c9d3de"/><path d="M0 50C80 24 170 24 253 42V60H0Z" fill="#434b6e"/></svg>
    <h3>Garage Door Repair</h3>
    <p>Lorem ipsum dolor sit amet, consectetuer adipiscing elit, sed diam nonummy nibh euismod</p>
    <div class="service-more">+</div>
  </article>
  <article class="abs service-card" style="left:337px">
    <div class="service-photo" role="img" aria-label="Garage door opener rail inside a garage" style="background:linear-gradient(135deg,#cfd4da,#7c8591)"></div>
    <svg class="service-wave" viewBox="0 0 253 60" preserveAspectRatio="none"><path d="M0 30C80 0 170 0 253 22V60H0Z" fill="#fff"/><path d="M0 42C80 14 170 14 253 34V60H0Z" fill="#c9d3de"/><path d="M0 50C80 24 170 24 253 42V60H0Z" fill="#434b6e"/></svg>
    <h3>Garage Door Openers</h3>
    <p>Lorem ipsum dolor sit amet, consectetuer adipiscing elit, sed diam nonummy nibh euismod</p>
    <div class="service-more">+</div>
  </article>
  <article class="abs service-card" style="left:612px">
    <div class="service-photo" role="img" aria-label="Modern glass panel garage door on a brick house" style="background:linear-gradient(135deg,#8a6a52,#3f3a40)"></div>
    <svg class="service-wave" viewBox="0 0 253 60" preserveAspectRatio="none"><path d="M0 30C80 0 170 0 253 22V60H0Z" fill="#fff"/><path d="M0 42C80 14 170 14 253 34V60H0Z" fill="#c9d3de"/><path d="M0 50C80 24 170 24 253 42V60H0Z" fill="#434b6e"/></svg>
    <h3>New Garage Doors</h3>
    <p>Lorem ipsum dolor sit amet, consectetuer adipiscing elit, sed diam nonummy nibh euismod</p>
    <div class="service-more">+</div>
  </article>
  <article class="abs service-card" style="left:887px">
    <div class="service-photo" role="img" aria-label="Close-up of a garage door torsion spring" style="background:linear-gradient(135deg,#c0642a,#6e3416)"></div>
    <svg class="service-wave" viewBox="0 0 253 60" preserveAspectRatio="none"><path d="M0 30C80 0 170 0 253 22V60H0Z" fill="#fff"/><path d="M0 42C80 14 170 14 253 34V60H0Z" fill="#c9d3de"/><path d="M0 50C80 24 170 24 253 42V60H0Z" fill="#434b6e"/></svg>
    <h3>Broken Springs</h3>
    <p>Lorem ipsum dolor sit amet, consectetuer adipiscing elit, sed diam nonummy nibh euismod</p>
    <div class="service-more">+</div>
  </article>
</section>

<section>
  <div class="abs band"></div>
  <h2 class="abs section-title welcome-title">Welcome to Cedar Ridge Overhead Doors</h2>
  <p class="abs welcome-text">Lorem ipsum dolor sit amet, consectetuer adipiscing elit, sed diam nonummy nibh euismod tincidunt utoreet dolore magna aliquam erat volutpat. Ut wisi enim ad minim veniam, quis nostrud exerci tation ullamcorper suscipit lobortis nisl ut aliquip ex ea commodo consequat. autem vel eum iriure dolor in hendrerit inlputate velit esse molestie consequat, vel illum dolore eu feugiat nulla facilisis at vero eros et accumsan et iustodio dignissim qui blandit tincidunt ut laoreet dolore magna aliquam erat volutpat. Ut wisi enim ad minim veniam, quis praesent luptatum zzril delenit augue duis dolore te feugait nulla facilisi.eu feugi nullaml facilisis at vero eros et accumsan et iusto facilisi. ate velit esse molestie consequat. nonummy nibh am nonummy nibh euism tinciduntl ut laoreet dolore maex ea commodo consequat. Duis autem v eummu iriure dolor in hendrerit</p>
  <div class="abs btn read-more">Read More</div>

  <h2 class="abs section-title inquiry-title">Quick Inquiry</h2>
  <div class="abs field" style="top:1207px"><div class="ico"><svg width="14" height="14" viewBox="0 0 14 14"><circle cx="7" cy="4.5" r="3" fill="#b3bcc6"/><path d="M1 14c0-4 3-6 6-6s6 2 6 6Z" fill="#b3bcc6"/></svg></div><span>Name</span></div>
  <div class="abs field" style="top:1251px"><div class="ico"><svg width="14" height="11" viewBox="0 0 14 11"><rect x=".5" y=".5" width="13" height="10" fill="none" stroke="#b3bcc6"/><path d="M.5.5 7 6l6.5-5.5" fill="none" stroke="#b3bcc6"/></svg></div><span>Email</span></div>
  <div class="abs field" style="top:1295px"><div class="ico"><svg width="14" height="14" viewBox="0 0 14 14"><path d="M3 1c1-.5 1.6.3 2 1l.7 1.4c.3.6 0 1.1-.4 1.5l-.6.5c.6 1.4 1.7 2.5 3 3.1l.5-.6c.4-.5 1-.6 1.5-.3l1.5.8c.7.4 1 1.1.6 1.8-1.5 2.2-4 1.3-6.2-.8C3.4 7.2 1.2 3.3 3 1z" fill="#b3bcc6"/></svg></div><span>Phone</span></div>
  <div class="abs field msg" style="top:1340px"><div class="ico"><svg width="14" height="14" viewBox="0 0 14 14"><rect x=".5" y="2.5" width="11" height="11" fill="none" stroke="#b3bcc6"/><path d="M5 9l1-3 7-6 1 1-7 6z" fill="#b3bcc6"/></svg></div><span>Message</span></div>
  <div class="abs btn submit">Submit</div>
</section>

<section>
  <h2 class="abs section-title col-title testi-title">Client Testimonials<span class="pager" style="position:absolute;right:0;top:2px">‹›</span></h2>
  <div class="abs divider"></div>
  <blockquote class="abs quote">“ Lorem ipsum dolor sit amet consetug e sed diay nibh euismodl tincidunt ut laoreet dolore magam er vol wisi enim ad minim veniam quis nostrud exerci the tationorem ipsum dolor sit ametee sed diammmy nibh euismd tincidunt ut laoreet dolore magna aliqur volpatl tiidunt ut laoreet dolore magna aliqur volpatl ”</blockquote>
  <svg class="abs quote-tail" viewBox="0 0 120 26"><path d="M0 0H120L100 26 80 0Z" fill="#d3dde4"/></svg>
  <div class="abs avatar" role="img" aria-label="Portrait of a satisfied client"></div>
  <div class="abs testi-name">Lorem Ipsum Dolor</div>

  <h2 class="abs section-title col-title offer-title">Special Offer<span class="pager" style="position:absolute;right:0;top:2px">‹›</span></h2>
  <div class="abs offer-sub">SAME DAY GARAGE DOOR REPAIR &amp; SERVICE</div>
  <p class="abs offer-text">Fast – Affordable – Professional – No Additional Charge For Weekends – 24 Hour Emergency Service Available</p>
  <div class="abs offer-box">
    <div class="price">$60 OFF</div>
    <div class="what">SPRING REPLACEMENT</div>
    <div class="note">$60 off Replacement of Two Garage Door Springs</div>
    <div class="dots"><i></i><i></i><i></i><i></i></div>
  </div>
</section>

<footer>
  <svg class="abs footer-wave" viewBox="0 0 1200 200" preserveAspectRatio="none">
    <path d="M0 185C400 160 800 110 1200 0V200H0Z" fill="#434b6e"/>
    <path d="M0 130C300 190 700 140 1200 10V60C800 160 350 200 0 150Z" fill="#a8bccb"/>
    <path d="M0 150C350 200 800 160 1200 60V80C800 175 350 215 0 170Z" fill="#fff" opacity=".8"/>
  </svg>
  <div class="abs badge badge-award" role="img" aria-label="Service award seal"></div>
  <div class="abs badge-rect" role="img" aria-label="Accreditation badge"></div>
  <div class="abs badge-round" role="img" aria-label="Review listing badge"></div>

  <div class="abs footer">
    <h4 class="f-title" style="left:60px">Quick Links</h4>
    <ul class="f-links">
      <li>Home</li><li>Openers</li><li>Garage Doors</li><li>Broken Springs</li><li>Garage Door Repair</li><li>Blog</li><li>Contact Us</li>
    </ul>
    <div class="f-sep" style="left:250px"></div>

    <h4 class="f-title" style="left:308px;width:218px">Contact Details</h4>
    <div class="f-contact" style="top:108px"><svg width="12" height="16" viewBox="0 0 12 16"><path d="M6 0a6 6 0 0 1 6 6c0 4-6 10-6 10S0 10 0 6a6 6 0 0 1 6-6z" fill="#fff"/><circle cx="6" cy="6" r="2.2" fill="#434b6e"/></svg><div><b>Cedar Ridge Overhead</b><br>4180 Alder Park Blvd, Denver<br>CO 80021</div></div>
    <div class="f-contact" style="top:193px"><svg width="14" height="14" viewBox="0 0 14 14"><path d="M3 1c1-.5 1.6.3 2 1l.7 1.4c.3.6 0 1.1-.4 1.5l-.6.5c.6 1.4 1.7 2.5 3 3.1l.5-.6c.4-.5 1-.6 1.5-.3l1.5.8c.7.4 1 1.1.6 1.8-1.5 2.2-4 1.3-6.2-.8C3.4 7.2 1.2 3.3 3 1z" fill="#fff"/></svg><div>555-014-2290</div></div>
    <div class="f-contact" style="top:246px"><svg width="14" height="11" viewBox="0 0 14 11"><rect width="14" height="11" fill="#fff"/><path d="M0 0 7 6l7-6" fill="none" stroke="#434b6e"/></svg><div>info@cedarridgeoverhead.example</div></div>
    <div class="f-sep" style="left:580px"></div>

    <h4 class="f-title" style="left:639px;width:223px">Location Map</h4>
    <div class="f-map" role="img" aria-label="Street map showing the shop location"></div>
    <div class="f-sep" style="left:916px"></div>

    <div class="f-logo"><div class="mark"></div><span>Cedar Ridge Overhead</span></div>
  </div>

  <div class="abs bottombar">
    <span>Copyright © 2016 Cedar Ridge Overhead.&nbsp; All rights reserved.</span>
    <div class="social">
      <i style="background:#3b5998"></i><i style="background:#3aa9e0"></i><i style="background:#1b86bd"></i><i style="background:#d34836"></i><i style="background:#e52d27"></i><i style="background:#f0892a"></i>
    </div>
  </div>
</footer>

</body>
</html>
```